Back Pain

Need a flyer similar to the attached draft. This is to be handed out to prospective patients. Note that Artwell Studio has already designed the logo. If you need a copy please contact me

```html
<!DOCTYPE html>
<html lang="en">
<head>
<meta charset="utf-8">
<title>Spine Ease Clinic – Tech Neck Flyer</title>
<link rel="stylesheet" href="https://fonts.googleapis.com/css2?family=Roboto+Condensed:wght@400;700;900&family=Oswald:wght@500;600&display=swap">
<style>
  :root {
    --navy-deep: #0a1644;
    --navy: #13296b;
    --navy-bright: #1f45a0;
    --sky: #2aa9e6;
    --sky-light: #3fc1f0;
    --teal: #2fb3c6;
    --green: #7cc242;
    --yellow: #ffe92b;
    --red: #e5232b;
    --white: #ffffff;
    --ink: #0b1a4a;
  }
  html, body { margin: 0; padding: 0; overflow: hidden; }
  body { width: 855px; height: 1200px; background: var(--navy-deep); }
  .flyer {
    position: relative; width: 855px; height: 1200px; overflow: hidden;
    font-family: "Roboto Condensed", "Arial Narrow", sans-serif; color: var(--white);
    background:
      linear-gradient(115deg, transparent 0 38%, rgba(70,120,220,.18) 38% 52%, transparent 52%),
      linear-gradient(115deg, transparent 0 60%, rgba(70,120,220,.12) 60% 70%, transparent 70%),
      linear-gradient(180deg, var(--navy) 0%, var(--navy-bright) 45%, var(--navy) 75%, var(--navy-deep) 100%);
  }
  .abs { position: absolute; }
  .shapes { position: absolute; left: 0; top: 0; }

  .brand { left: 0; width: 855px; top: 178px; text-align: center; }
  .brand-name { font-weight: 700; font-size: 37px; letter-spacing: .5px; color: var(--sky-light); line-height: 1; }
  .brand-role { margin-top: 4px; font-size: 19px; letter-spacing: 2.5px; color: var(--green); font-weight: 700; }
  .phone { left: 0; width: 855px; top: 252px; text-align: center; font-size: 24px; font-weight: 700; }
  .phone svg { vertical-align: -4px; margin-right: 8px; }

  .figure-area {
    left: 28px; top: 322px; width: 240px; height: 605px;
    background: linear-gradient(180deg, #e6e8ee, #c9ccd6);
    border-radius: 110px 110px 40px 40px; opacity: .95;
  }

  .symptom {
    position: absolute; left: 190px; height: 30px; line-height: 30px;
    padding: 0 22px 0 22px; border-radius: 0 15px 15px 0;
    background: var(--sky-light); color: var(--white);
    font-size: 13px; font-weight: 700; white-space: nowrap;
  }

  .tech-neck { left: 614px; top: 330px; font-family: "Oswald", sans-serif; font-weight: 600; font-size: 44px; color: var(--green); letter-spacing: .5px; }

  .usage-box { left: 338px; top: 457px; width: 238px; height: 193px; border-radius: 12px; background: rgba(255,255,255,.2); }
  .usage-text { left: 338px; width: 238px; top: 556px; text-align: center; font-weight: 700; line-height: 1.15; }
  .usage-text .small { font-size: 15px; }
  .usage-text .big { font-size: 22px; }

  .tilt-note { left: 629px; top: 462px; font-size: 13.5px; font-weight: 700; line-height: 1.2; }
  .tilt-axis { left: 626px; top: 642px; font-size: 12.5px; font-weight: 700; color: var(--yellow); }
  .tilt-degrees { left: 626px; top: 622px; font-size: 15px; font-weight: 700; word-spacing: 10px; }
  .pressure-axis { left: 757px; top: 540px; width: 160px; font-size: 12.5px; font-weight: 700; color: var(--yellow); transform: rotate(-90deg); text-align: center; }

  .message { left: 230px; width: 600px; top: 712px; text-align: center; font-weight: 700; text-transform: uppercase; line-height: 1.12; }
  .message .l1 { font-size: 30px; }
  .message .l2 { font-size: 21px; }
  .message .l3 { font-size: 33px; }
  .message .l4 { font-size: 25px; }
  .hl { color: var(--yellow); }

  .doctor { left: 39px; top: 980px; font-weight: 700; font-size: 27px; line-height: 1.55; color: var(--yellow); }
  .doctor .bullet { position: absolute; left: 0; top: 12px; width: 17px; height: 17px; background: var(--ink); }
  .doctor .lines { padding-left: 32px; }

  .offer-badge { left: 593px; top: 934px; width: 128px; height: 62px; border-radius: 50%; background: var(--white); text-align: center; line-height: 62px; }
  .offer-badge .pct { font-family: "Oswald", sans-serif; font-weight: 600; font-size: 40px; color: var(--red); }
  .offer-badge .off { display: inline-block; font-size: 14px; font-weight: 700; color: var(--red); line-height: 1; vertical-align: 6px; }
  .offer-text { left: 500px; width: 355px; top: 1002px; text-align: center; font-weight: 700; font-size: 21px; color: var(--ink); line-height: 1.6; }

  .footer { left: 0; top: 1132px; width: 855px; height: 68px; background: linear-gradient(90deg, var(--teal), #3cc0cf); }
  .footer span { position: absolute; top: 20px; font-size: 22px; font-weight: 700; }
  .footer .email { left: 42px; }
  .footer .web { left: 482px; }
</style>
</head>
<body>
<main class="flyer">
  <svg class="shapes" width="855" height="1200" viewBox="0 0 855 1200" aria-hidden="true">
    <circle cx="428" cy="96" r="66" fill="none" stroke="#3fc1f0" stroke-width="6"/>
    <g fill="none" stroke="#3fc1f0" stroke-width="6" opacity=".8">
      <polyline points="398,338 414,356 398,374"/>
      <polyline points="424,338 440,356 424,374"/>
      <polyline points="450,338 466,356 450,374"/>
      <polyline points="476,338 492,356 476,374"/>
      <polyline points="502,338 518,356 502,374"/>
      <polyline points="528,338 544,356 528,374"/>
      <polyline points="554,338 570,356 554,374"/>
      <polyline points="580,338 596,356 580,374"/>
    </g>
    <rect x="0" y="922" width="855" height="210" fill="#0e2260"/>
    <polygon points="330,922 420,922 560,1132 470,1132" fill="#13296b"/>
    <polygon points="410,922 855,922 855,1132 550,1132" fill="#2aa9e6"/>
  </svg>

  <div class="abs brand">
    <div class="brand-name">SPINE EASE CLINIC</div>
    <div class="brand-role">DR SAM WHITFORD - CHIROPRACTOR</div>
  </div>
  <div class="abs phone">
    <svg width="22" height="22" viewBox="0 0 22 22"><circle cx="11" cy="11" r="11" fill="#3fc1f0"/><path d="M7 5.5l2.2-.4 1.2 3-1.4 1a7 7 0 003.6 3.6l1-1.4 3 1.2-.4 2.2c-5 .4-9.6-4.2-9.2-9.2z" fill="#fff"/></svg>0400 555 018
  </div>

  <div class="abs figure-area" role="img" aria-label="Silhouette of a person walking while looking down at a phone"></div>

  <div class="symptom" style="top:337px;">HEADACHES</div>
  <div class="symptom" style="top:379px;">NECK PAIN</div>
  <div class="symptom" style="top:420px;">SHOULDER PAIN</div>
  <div class="symptom" style="top:463px;">BACK PAIN</div>
  <div class="symptom" style="top:525px;">ARM &amp; HAND PAIN</div>
  <div class="symptom" style="top:567px;">SCIATICA</div>

  <div class="abs tech-neck">TECH NECK</div>

  <div class="abs usage-box"></div>
  <svg class="shapes" width="855" height="1200" viewBox="0 0 855 1200" role="img" aria-label="Pie chart of daily device use">
    <circle cx="454" cy="505" r="40" fill="#c8cbd6"/>
    <path d="M454 505 L454 465 A40 40 0 0 1 482 533 Z" fill="#1c2b66"/>
  </svg>
  <div class="abs usage-text">
    <div class="small">THE AVERAGE PERSON SPENDS</div>
    <div class="big">8-11 HOURS PER DAY</div>
    <div class="small">USING ELECTRONIC DEVICES</div>
  </div>

  <div class="abs tilt-note">AS THE HEAD TILTS FORWARD,<br>MORE FORCE IS PLACED<br>ON THE SPINE</div>
  <svg class="shapes" width="855" height="1200" viewBox="0 0 855 1200" role="img" aria-label="Bar chart of spine pressure by head tilt">
    <rect x="611" y="546" width="16" height="48" rx="6" fill="#ffffff" role="img" aria-label="Side profile of a head"/>
    <rect x="631" y="588" width="24" height="28" fill="#e5232b"/>
    <rect x="668" y="560" width="24" height="56" fill="#e5232b"/>
    <rect x="703" y="525" width="24" height="91" fill="#e5232b"/>
    <rect x="738" y="507" width="24" height="109" fill="#e5232b"/>
    <rect x="775" y="483" width="24" height="133" fill="#e5232b"/>
  </svg>
  <div class="abs tilt-degrees">0° 15° 30° 45° 60°</div>
  <div class="abs tilt-axis">DEGREES OF FORWARD HEAD TILT</div>
  <div class="abs pressure-axis">PRESSURE ON SPINE (LBS)</div>

  <div class="abs message">
    <div class="l1"><span class="hl">CHIROPRACTIC CARE</span> CAN HELP</div>
    <div class="l2">CORRECT AND PREVENT THESE PROBLEMS</div>
    <div class="l3">BY RESTORING <span class="hl">AND</span> MAINTAINING</div>
    <div class="l4">PROPER ALIGNMENT <span class="hl">OF THE</span> NECK</div>
  </div>

  <div class="abs doctor">
    <span class="bullet"></span>
    <div class="lines">Dr. Samuel Whitford<br>Now in Harbourton at<br>42, Quay Rd, Harbour Suites</div>
  </div>

  <div class="abs offer-badge"><span class="pct">50</span><span class="off">%<br>OFF</span></div>
  <div class="abs offer-text">on Initial Consultation<br>If you book online @<br>www.spineeaseclinic.example<br>* Choose “Tech Neck” Option</div>

  <div class="abs footer">
    <span class="email">sam@spineeaseclinic.example</span>
    <span class="web">www.spineeaseclinic.example</span>
  </div>
</main>
</body>
</html>
```